Bright Fern Custom Homes business card. Double sided. Modern. professional

Bright Fern Custom Homes
contemporary modern design with our logo /
Double sided with all our contact information
Use same Green colors as in our Logo. Contemporary logo that grabs your attention. Visually pleasing and balanced. Easy to read, and Vibrant. Would love an option for rounded edges. Embossed logo would be amazing.
Contact Information for Business Card
Dana Welk Owner / General Contractor Bright Fern Custom Homes p: 704.552.1830 m: 912.648.2071 e: brightferncustomhomes@mailbox.example w: www.brightferncustomhomes.example 218 Pryor Meadow Lane Fernwick, TN 29041

```html
<!DOCTYPE html>
<html lang="en">
<head>
<meta charset="utf-8">
<title>Bright Fern Custom Homes – Business Card</title>
<link rel="stylesheet" href="https://fonts.googleapis.com/css2?family=Montserrat:wght@400;500&family=Oswald:wght@300;600&display=swap">
<style>
  :root {
    --page-bg: #dcdcdc;
    --card-bg: #ffffff;
    --brand-green: #5c9e14;
    --ink: #1e1e1e;
  }
  * { box-sizing: border-box; margin: 0; padding: 0; }
  html, body { width: 1200px; height: 1200px; overflow: hidden; }
  body {
    background: var(--page-bg);
    font-family: "Montserrat", sans-serif;
    color: var(--ink);
    display: flex;
    flex-direction: column;
    align-items: center;
    justify-content: center;
    gap: 60px;
  }
  .card {
    position: relative;
    width: 760px;
    height: 480px;
    background: var(--card-bg);
  }
  .brand-lockup {
    position: absolute;
    display: flex;
    flex-direction: column;
    align-items: center;
    gap: 14px;
    color: var(--brand-green);
    font-family: "Montserrat", sans-serif;
    font-weight: 500;
    font-size: 22px;
    letter-spacing: 0.12em;
    line-height: 1.25;
    text-align: center;
    text-transform: uppercase;
  }
  .brand-mark {
    width: 64px;
    height: 64px;
    border-radius: 50%;
    background: var(--brand-green);
  }
  .card-front .brand-lockup {
    left: 0;
    width: 315px;
    top: 150px;
  }
  .divider {
    position: absolute;
    left: 315px;
    top: 0;
    width: 3px;
    height: 100%;
    background: var(--brand-green);
  }
  .details {
    position: absolute;
    left: 335px;
    top: 112px;
  }
  .person-name {
    font-family: "Oswald", sans-serif;
    font-size: 38px;
    line-height: 1;
    text-transform: uppercase;
    letter-spacing: 0.02em;
  }
  .person-name .first { font-weight: 600; color: var(--brand-green); }
  .person-name .last { font-weight: 300; color: var(--ink); }
  .person-role {
    font-size: 25px;
    font-weight: 400;
    margin-top: 4px;
  }
  .contact-list {
    list-style: none;
    margin-top: 44px;
    display: flex;
    flex-direction: column;
    gap: 16px;
    font-size: 16.5px;
    line-height: 1.35;
  }
  .contact-list li {
    display: flex;
    align-items: flex-start;
    gap: 12px;
  }
  .contact-icon {
    flex: none;
    width: 13px;
    height: 13px;
    margin-top: 4px;
    fill: var(--ink);
  }
  .card-back .brand-lockup {
    left: 55px;
    width: 250px;
    top: 255px;
  }
</style>
</head>
<body>

  <section class="card card-front" aria-label="Business card front">
    <div class="brand-lockup">
      <span class="brand-mark"></span>
      <span class="brand-name">Bright Fern<br>Custom Homes</span>
    </div>
    <div class="divider"></div>
    <div class="details">
      <h1 class="person-name"><span class="first">Dana</span> <span class="last">Welk</span></h1>
      <p class="person-role">Owner</p>
      <ul class="contact-list">
        <li>
          <svg class="contact-icon" viewBox="0 0 24 24" aria-hidden="true"><path d="M12 1a8 8 0 0 0-8 8c0 6 8 14 8 14s8-8 8-14a8 8 0 0 0-8-8zm0 11a3 3 0 1 1 0-6 3 3 0 0 1 0 6z"/></svg>
          <span>218 Pryor Meadow Lane<br>Fernwick, TN 29041</span>
        </li>
        <li>
          <svg class="contact-icon" viewBox="0 0 24 24" aria-hidden="true"><path d="M6.6 10.8a15.1 15.1 0 0 0 6.6 6.6l2.2-2.2a1 1 0 0 1 1-.25 11.4 11.4 0 0 0 3.6.57 1 1 0 0 1 1 1V20a1 1 0 0 1-1 1A17 17 0 0 1 3 4a1 1 0 0 1 1-1h3.5a1 1 0 0 1 1 1c0 1.25.2 2.45.57 3.57a1 1 0 0 1-.25 1z"/></svg>
          <span>704.552.1830, 912.648.2071</span>
        </li>
        <li>
          <svg class="contact-icon" viewBox="0 0 24 24" aria-hidden="true"><path d="M2 5h20v14H2zm2 2v.5l8 5 8-5V7l-8 5z"/></svg>
          <span>brightferncustomhomes@mailbox.example</span>
        </li>
        <li>
          <svg class="contact-icon" viewBox="0 0 24 24" aria-hidden="true"><path d="M5 2l14 12h-7l4 8-3 1.5-4-8L5 20z"/></svg>
          <span>www.brightferncustomhomes.example</span>
        </li>
      </ul>
    </div>
  </section>

  <section class="card card-back" aria-label="Business card back">
    <div class="brand-lockup">
      <span class="brand-mark"></span>
      <span class="brand-name">Bright Fern<br>Custom Homes</span>
    </div>
  </section>

</body>
</html>
```